Steady Harbor Claims Group Business card

Need a business card that stands out that includes name of company,(above) Owners name Moira Lindqvist phone#517-362-4408 email# SteadyHarborCG@mailvane.com and website www.Steadyharborclaimsgroup.net. This is a medical billing company so the card has to relate to that or relate to increasing revenue

```html
<!DOCTYPE html>
<html lang="en">
<head>
<meta charset="utf-8">
<title>Steady Harbor Claims Group – Business Card</title>
<link href="https://fonts.googleapis.com/css2?family=Arimo:wght@400;700&display=swap" rel="stylesheet">
<style>
  :root {
    --page: #e8e5e0;
    --card-white: #ffffff;
    --card-grey: #ececec;
    --navy: #1a4a8a;
    --navy-deep: #0d336b;
    --navy-light: #23609f;
    --green: #78bd2e;
    --green-light: #a9d66c;
    --ink: #505050;
    --white: #ffffff;
  }
  * { box-sizing: border-box; margin: 0; padding: 0; }
  html, body {
    width: 1200px; height: 950px; overflow: hidden;
    background: var(--page);
    font-family: "Arimo", Arial, sans-serif;
  }
  .card {
    position: absolute; left: 250px; width: 700px; height: 400px;
    border-radius: 4px; overflow: hidden;
    box-shadow: 0 6px 18px rgba(0,0,0,.18);
  }
  /* Front */
  .card-front {
    top: 45px;
    background: linear-gradient(160deg, var(--card-white) 45%, var(--card-grey) 100%);
  }
  .name-band {
    position: absolute; left: 0; top: 70px; width: 100%; height: 62px;
    background: linear-gradient(90deg, var(--green) 0%, var(--green) 52%, var(--green-light) 62%, var(--navy) 64%, var(--navy) 100%);
  }
  .brand-block {
    position: absolute; left: 448px; top: 70px; width: 252px; height: 110px;
    background: var(--navy);
  }
  .holder {
    position: absolute; left: 36px; top: 80px; color: var(--navy);
  }
  .holder-name { font-size: 21px; font-weight: 700; line-height: 1.2; }
  .holder-title { font-size: 13px; line-height: 1.3; }
  .brand-name {
    position: absolute; right: 24px; top: 192px;
    font-size: 22px; font-weight: 700; letter-spacing: .5px;
    text-transform: uppercase; color: var(--navy); text-align: right; line-height: 1.15;
  }
  .contact {
    position: absolute; left: 130px; top: 268px;
    font-size: 16px; color: var(--ink); line-height: 1.9;
  }
  .contact .label { color: var(--navy); font-weight: 700; margin-right: 4px; }
  .contact .gap { display: inline-block; width: 14px; }
  .contact .web { padding-left: 36px; }
  /* Back */
  .card-back {
    top: 490px;
    background: linear-gradient(125deg, var(--navy-deep) 0%, var(--navy) 55%, var(--navy-light) 100%);
    display: flex; flex-direction: column; align-items: center; justify-content: center;
    color: var(--white); text-align: center;
  }
  .back-brand {
    font-size: 32px; font-weight: 700; letter-spacing: 1px;
    text-transform: uppercase; line-height: 1.15;
  }
  .back-web { margin-top: 18px; font-size: 16px; }
</style>
</head>
<body>
  <section class="card card-front">
    <div class="name-band"></div>
    <div class="brand-block"></div>
    <div class="holder">
      <p class="holder-name">Moira Lindqvist</p>
      <p class="holder-title">Owners</p>
    </div>
    <p class="brand-name">Steady Harbor<br>Claims Group</p>
    <div class="contact">
      <p><span class="label">P :</span>517-362-4408<span class="gap"></span><span class="label">E :</span>SteadyHarborCG@mailvane.com</p>
      <p class="web"><span class="label">W :</span>www.Steadyharborclaimsgroup.net</p>
    </div>
  </section>

  <section class="card card-back">
    <p class="back-brand">Steady Harbor<br>Claims Group</p>
    <p class="back-web">www.Steadyharborclaimsgroup.net</p>
  </section>
</body>
</html>
```